Hedge fund needs power point design for marketing pitch

We need a designer to make our power point pitch more aesthetically appealing to potential clients. We will be marketing our hedge fund to high net worth individuals and financial institutions. The ideal design will look professional and project confidence to our potential clients. We have attached a rough outline of what we have completed so far. We have also attached example cover pages for 2 pitch books produced by our competitors.

Target Market(s)

Financial institutions and wealthy investors

Industry/Entity Type

Finance

Requirements
Must have
• must use our logo and current slides. Must look professional

```html
<!DOCTYPE html>
<html lang="en">
<head>
<meta charset="utf-8">
<title>Ashbury Capital Management – Pitch Slides</title>
<link rel="stylesheet" href="https://fonts.googleapis.com/css2?family=Open+Sans:ital,wght@0,300;0,400;0,600;0,700;1,600&family=Tinos&display=swap">
<style>
  :root {
    --backdrop: #525254;
    --slide: #ffffff;
    --ink: #1e1e1e;
    --body: #2b2b2b;
    --gold: #c4962f;
    --dark: #222222;
    --frame: #c8c8c8;
  }
  * { box-sizing: border-box; margin: 0; padding: 0; }
  html, body { width: 1200px; height: 844px; overflow: hidden; }
  body {
    background: var(--backdrop);
    position: relative;
    font-family: "Open Sans", Arial, sans-serif;
    color: var(--body);
  }
  .slide {
    position: absolute;
    width: 512px;
    height: 362px;
    background: var(--slide);
    overflow: hidden;
  }
  .slide--disclaimer { left: 66px; top: 47px; }
  .slide--objective  { left: 620px; top: 47px; }
  .slide--strategy   { left: 66px; top: 432px; }
  .slide--bios       { left: 620px; top: 432px; }

  .slide__title {
    position: absolute; left: 0; right: 0; top: 16px;
    text-align: center;
    font-weight: 300;
    font-size: 22px;
    color: var(--ink);
  }
  .slide__subtitle {
    position: absolute; left: 0; right: 0; top: 48px;
    text-align: center;
    font-weight: 700;
    font-size: 9px;
    letter-spacing: 0.4px;
    color: var(--gold);
  }
  .slide__rule {
    position: absolute; left: 75px; width: 362px; top: 70px; height: 10px;
    background: radial-gradient(ellipse at 50% 0%, rgba(0,0,0,0.45) 0%, rgba(0,0,0,0.12) 35%, rgba(0,0,0,0) 70%);
  }
  .brand {
    position: absolute; left: 50px; top: 323px;
    display: flex; align-items: center; gap: 4px;
    font-weight: 700;
    font-size: 10px;
    letter-spacing: 0.8px;
    color: var(--ink);
  }
  .brand__dot { width: 7px; height: 7px; border-radius: 50%; background: var(--gold); }
  .slide__copyright {
    position: absolute; right: 13px; top: 342px;
    font-family: "Tinos", "Times New Roman", serif;
    font-size: 6.5px;
    color: var(--ink);
  }

  /* Disclaimer */
  .disclaimer__photo {
    position: absolute; left: 49px; top: 116px; width: 92px; height: 91px;
    background: linear-gradient(160deg, #cfe0f2 0%, #5d86b6 45%, #1e3f6e 100%);
  }
  .disclaimer__text {
    position: absolute; left: 156px; top: 113px; width: 300px;
    font-size: 6.9px; line-height: 10px;
  }
  .disclaimer__text p + p { margin-top: 10px; }

  /* Objective */
  .objective__item { position: absolute; left: 103px; display: flex; }
  .objective__item--one { top: 120px; }
  .objective__item--two { top: 193px; }
  .objective__icon {
    width: 44px; height: 44px; border-radius: 50%;
    border: 1px solid var(--gold);
    display: flex; align-items: center; justify-content: center;
    flex: none;
  }
  .objective__copy { margin-left: 9px; width: 215px; font-size: 6.9px; line-height: 10px; }
  .bullets { list-style: none; }
  .bullets li { position: relative; padding-left: 8px; margin-top: 9px; }
  .bullets li::before {
    content: ""; position: absolute; left: 0; top: 2px;
    border-left: 5px solid var(--gold);
    border-top: 3px solid transparent; border-bottom: 3px solid transparent;
  }

  /* Strategy */
  .step { position: absolute; top: 103px; width: 92px; }
  .step--solve   { left: 69px; }
  .step--params  { left: 174px; }
  .step--answer  { left: 277px; }
  .step--trade   { left: 381px; }
  .step__badge {
    position: relative; width: 62px; height: 62px; border-radius: 50%;
    display: flex; align-items: center; justify-content: center;
  }
  .step__badge--gold { background: var(--gold); }
  .step__badge--dark { background: var(--dark); }
  .step__pointer {
    position: absolute; left: 22px; bottom: -9px; width: 18px; height: 18px;
    border-radius: 50%; background: #fff; border: 1px solid #bbb;
    display: flex; align-items: center; justify-content: center;
  }
  .step__pointer::after {
    content: ""; border-top: 5px solid var(--dark);
    border-left: 4px solid transparent; border-right: 4px solid transparent;
  }
  .step__text { margin: 21px 0 0 -9px; width: 90px; font-size: 7px; line-height: 10px; }
  .step__text .bullets li { margin-top: 3px; }

  /* Bios */
  .member { position: absolute; top: 89px; width: 98px; }
  .member--1 { left: 44px; }
  .member--2 { left: 158px; }
  .member--3 { left: 273px; }
  .member--4 { left: 388px; }
  .member__frame { width: 98px; height: 69px; border: 1px solid var(--frame); padding: 5px; }
  .member__photo {
    width: 100%; height: 100%;
    background: linear-gradient(180deg, #f2f2f2 0%, #e2cdb8 55%, #c9a98b 100%);
  }
  .member__name { margin-top: 8px; font-weight: 700; font-size: 7.8px; color: var(--ink); }
  .member__role { font-weight: 600; font-style: italic; font-size: 6.6px; color: var(--gold); margin-top: 1px; }
  .member__bio { margin-top: 5px; font-size: 6.8px; line-height: 9.6px; }
</style>
</head>
<body>

<!-- Disclaimer -->
<section class="slide slide--disclaimer">
  <h1 class="slide__title">DISCLAIMER</h1>
  <div class="slide__rule"></div>
  <div class="disclaimer__photo" role="img" aria-label="Photo of glass office towers seen from below"></div>
  <div class="disclaimer__text">
    <p>Lorem ipsum &nbsp;is a simply dummy text for your printing setting Lorem ipsum is a simply dummy text for Lorem ipsum &nbsp;is a simply dummy text for your printing setting Lorem ipsum is a simply dummy text for Lorem ipsum &nbsp;is a simply dummy text for your printing setting Lorem ipsum is a simply</p>
    <p>dummy text for Lorem ipsum &nbsp;is a simply dummy text for your printing setting Lorem ipsum is a simply dummy text for dummy text for Lorem ipsum &nbsp;is a simply dummy text for your printing setting Lorem ipsum is a simply dummy text for<br>Lorem ipsum &nbsp;is a simply dummy text for your printing setting Lorem ipsum is a simply dummy text for Lorem ipsum &nbsp;is a simply dummy text for your printing setting Lorem ipsum is a simply dummy text for Lorem ipsum &nbsp;is a simply dummy text for your printing setting Lorem ipsum is a simply</p>
    <p>dummy text for Lorem ipsum &nbsp;is a simply dummy text for your printing setting Lorem ipsum is a simply dummy text for Lorem ipsum &nbsp;is a simply dummy text for your print-</p>
  </div>
  <div class="brand"><span class="brand__dot"></span>ASHBURY CAPITAL</div>
  <div class="slide__copyright">Copy right to Ashbury Capital Management LLC</div>
</section>

<!-- Investment objective -->
<section class="slide slide--objective">
  <h1 class="slide__title">INVESTMENT OBJECTIVE</h1>
  <div class="slide__subtitle">PUT YOUR SUB HEADINGS HERE</div>
  <div class="slide__rule"></div>
  <div class="objective__item objective__item--one">
    <div class="objective__icon">
      <svg width="24" height="22" viewBox="0 0 24 22">
        <rect x="2" y="14" width="4" height="7" fill="#222"/>
        <rect x="8" y="10" width="4" height="11" fill="#222"/>
        <rect x="14" y="7" width="4" height="14" fill="#222"/>
        <path d="M2 11 L9 5 L13 8 L20 2" stroke="#222" stroke-width="2" fill="none"/>
        <path d="M17 1 L22 1 L22 6 Z" fill="#222"/>
      </svg>
    </div>
    <div class="objective__copy">
      <p style="margin-top:4px">Profit from inefficiencies in equity and index options markets</p>
      <ul class="bullets">
        <li>Buy options that are underpriced</li>
        <li>Sell options that are overpriced</li>
      </ul>
    </div>
  </div>
  <div class="objective__item objective__item--two">
    <div class="objective__icon">
      <svg width="24" height="26" viewBox="0 0 24 26">
        <path d="M7 14 L3 24 L7 22 L9 25 L12 17 Z M17 14 L21 24 L17 22 L15 25 L12 17 Z" fill="#222"/>
        <circle cx="12" cy="10" r="8.5" fill="#222"/>
        <circle cx="12" cy="10" r="5" fill="none" stroke="#fff" stroke-width="1.3"/>
      </svg>
    </div>
    <div class="objective__copy">
      <p style="margin-top:4px">Achieve outsized and consistent returns by maintaining a small and nimble fund that can exploit price inefficiencies and move in and out of trades quickly</p>
    </div>
  </div>
  <div class="brand"><span class="brand__dot"></span>ASHBURY CAPITAL</div>
  <div class="slide__copyright">Copy right to Ashbury Capital Management LLC</div>
</section>

<!-- Investment strategy -->
<section class="slide slide--strategy">
  <h1 class="slide__title">INVESTMENT STRATEGY</h1>
  <div class="slide__subtitle">PUT YOUR SUB HEADINGS HERE</div>
  <div class="slide__rule"></div>

  <div class="step step--solve">
    <div class="step__badge step__badge--gold">
      <svg width="30" height="30" viewBox="0 0 30 30" aria-hidden="true">
        <rect x="2" y="2" width="26" height="26" rx="1" fill="#fff"/>
        <path d="M15 2 V8.5 a2.8 2.8 0 1 1 0 5.5 V16 M15 16 V21 a2.8 2.8 0 1 0 0 5.5 V28" fill="none" stroke="#c4962f" stroke-width="1.6"/>
        <path d="M2 15 H7.5 a2.8 2.8 0 1 0 5.5 0 H15 M15 15 H19 a2.8 2.8 0 1 1 5.5 0 H28" fill="none" stroke="#c4962f" stroke-width="1.6"/>
      </svg>
      <span class="step__pointer"></span>
    </div>
    <p class="step__text">Strategy derived from a dynamic optimization problem that maximizes returns within a given risk constraint.</p>
  </div>

  <div class="step step--params">
    <div class="step__badge step__badge--dark">
      <svg width="26" height="28" viewBox="0 0 26 28" aria-hidden="true">
        <path d="M6 2 H22 V26 H6 Z" fill="none" stroke="#fff" stroke-width="1.8" transform="rotate(-10 14 14)"/>
        <path d="M10 8 H18 M10 12 H18 M10 16 H16" stroke="#fff" stroke-width="1.6" transform="rotate(-10 14 14)"/>
        <path d="M2 22 L8 27 L12 21" fill="#fff"/>
      </svg>
      <span class="step__pointer"></span>
    </div>
    <div class="step__text">
      <p>Parameters/assumptions</p>
      <ul class="bullets">
        <li>Assume liquid markets</li>
        <li>Assume a price discount/premium on each trade (5-10%)</li>
      </ul>
    </div>
  </div>

  <div class="step step--answer">
    <div class="step__badge step__badge--gold">
      <svg width="30" height="30" viewBox="0 0 30 30" aria-hidden="true">
        <path d="M15 7 a7 7 0 0 1 4 12.7 V22 H11 V19.7 A7 7 0 0 1 15 7 Z" fill="none" stroke="#fff" stroke-width="1.8"/>
        <path d="M12 24.5 H18 M13 27 H17" stroke="#fff" stroke-width="1.6"/>
        <path d="M15 1 V4 M4 12 H7 M23 12 H26 M7 4 L9 6 M23 4 L21 6" stroke="#fff" stroke-width="1.6"/>
      </svg>
      <span class="step__pointer"></span>
    </div>
    <div class="step__text">
      <p>Solution - the optimization problem tells us:</p>
      <ul class="bullets">
        <li>When to buy or sell contracts</li>
        <li>Which contracts to buy or sell</li>
        <li>How many contracts to buy or sell</li>
      </ul>
    </div>
  </div>

  <div class="step step--trade">
    <div class="step__badge step__badge--dark">
      <svg width="30" height="30" viewBox="0 0 30 30" aria-hidden="true">
        <g transform="rotate(-20 15 15)">
          <path d="M9 4 H21 L24 9 V26 H6 V9 Z" fill="#fff"/>
          <circle cx="15" cy="8.5" r="1.8" fill="#222"/>
          <path d="M11 21 L19 13" stroke="#222" stroke-width="1.4"/>
          <circle cx="12" cy="14" r="1.7" fill="none" stroke="#222" stroke-width="1.2"/>
          <circle cx="18" cy="20" r="1.7" fill="none" stroke="#222" stroke-width="1.2"/>
        </g>
      </svg>
      <span class="step__pointer"></span>
    </div>
    <p class="step__text">We make trades based on these solutions while hitting the price discount/premium offered by the market.</p>
  </div>

  <div class="brand"><span class="brand__dot"></span>ASHBURY CAPITAL</div>
  <div class="slide__copyright">Copy right to Ashbury Capital Management LLC</div>
</section>

<!-- Managers bios -->
<section class="slide slide--bios">
  <h1 class="slide__title">MANAGERS BIOS</h1>
  <div class="slide__subtitle">PUT YOUR SUB HEADINGS HERE</div>
  <div class="slide__rule"></div>

  <article class="member member--1">
    <div class="member__frame"><div class="member__photo" role="img" aria-label="Portrait photo of a fund manager"></div></div>
    <h2 class="member__name">Name of the Member</h2>
    <p class="member__role">Designation</p>
    <p class="member__bio">Often times, TCPA rules and regulations are overlooked when the proper time and attention fails to be given to quality assurance. Whether it's your own call center or a call center providing you. leads, allow Clearline to assure the acceptable and appropriate</p>
  </article>
  <article class="member member--2">
    <div class="member__frame"><div class="member__photo" role="img" aria-label="Portrait photo of a fund manager"></div></div>
    <h2 class="member__name">Name of the Member</h2>
    <p class="member__role">Designation</p>
    <p class="member__bio">Often times, TCPA rules and regulations are overlooked when the proper time and attention fails to be given to quality assurance. Whether it's your own call center or a call center providing you. leads, allow Clearline to assure the acceptable and appropriate</p>
  </article>
  <article class="member member--3">
    <div class="member__frame"><div class="member__photo" role="img" aria-label="Portrait photo of a fund manager"></div></div>
    <h2 class="member__name">Name of the Member</h2>
    <p class="member__role">Designation</p>
    <p class="member__bio">Often times, TCPA rules and regulations are overlooked when the proper time and attention fails to be given to quality assurance. Whether it's your own call center or a call center providing you. leads, allow Clearline to assure the acceptable and appropriate</p>
  </article>
  <article class="member member--4">
    <div class="member__frame"><div class="member__photo" role="img" aria-label="Portrait photo of a fund manager"></div></div>
    <h2 class="member__name">Name of the Member</h2>
    <p class="member__role">Designation</p>
    <p class="member__bio">Often times, TCPA rules and regulations are overlooked when the proper time and attention fails to be given to quality assurance. Whether it's your own call center or a call center providing you. leads, allow Clearline to assure the acceptable and appropriate</p>
  </article>

  <div class="brand"><span class="brand__dot"></span>ASHBURY CAPITAL</div>
  <div class="slide__copyright">Copy right to Ashbury Capital Management LLC</div>
</section>

</body>
</html>
```